Business Consulting Business Card

professional business card with basic information (1) First and Last name (2) email address, (3) phone number, (4) website.

```html
<!DOCTYPE html>
<html lang="en">
<head>
<meta charset="utf-8">
<title>Tide Cove – Business Card</title>
<link rel="stylesheet" href="https://fonts.googleapis.com/css2?family=Montserrat:wght@400;500;600&display=swap">
<style>
  :root {
    --stage: #2b2b2d;
    --sky: #5bbde2;
    --lagoon: #46a8a6;
    --teal-text: #45b3cf;
    --ink: #1f2a36;
    --muted: #4a4f57;
    --paper: #ffffff;
    --edge: #111111;
  }
  * { box-sizing: border-box; margin: 0; padding: 0; }
  html, body {
    width: 1200px; height: 900px; overflow: hidden;
    background: var(--stage);
    font-family: "Montserrat", sans-serif;
  }
  .canvas { position: relative; width: 1200px; height: 900px; }

  .card {
    position: absolute; left: 320px; width: 560px; height: 320px;
    box-shadow: 0 12px 30px rgba(0,0,0,.45);
    overflow: hidden;
  }

  /* Front side */
  .card--front {
    top: 90px;
    background: linear-gradient(135deg, var(--sky) 0%, var(--lagoon) 100%);
    color: var(--paper);
  }
  .brand {
    display: flex; align-items: center; gap: 14px;
    font-weight: 500; letter-spacing: .28em; text-transform: uppercase;
  }
  .brand__dot { border-radius: 50%; flex: none; }
  .card--front .brand {
    position: absolute; left: 50%; top: 128px; transform: translateX(-50%);
    font-size: 28px; white-space: nowrap;
  }
  .card--front .brand__dot { width: 44px; height: 44px; background: var(--paper); }
  .website {
    position: absolute; left: 0; right: 0; bottom: 34px;
    text-align: center; font-size: 14px; font-weight: 600; letter-spacing: .02em;
  }

  /* Back side */
  .card--back { top: 470px; background: var(--paper); }
  .card--back .brand {
    position: absolute; left: 50%; top: 74px; transform: translateX(-50%);
    font-size: 22px; color: var(--ink); white-space: nowrap;
  }
  .card--back .brand__dot { width: 36px; height: 36px; background: var(--teal-text); }

  .details {
    position: absolute; left: 0; right: 0; top: 170px;
    display: flex; justify-content: center; align-items: center; gap: 28px;
  }
  .person { text-align: right; }
  .person__name { font-size: 17px; font-weight: 600; color: var(--teal-text); }
  .person__role { font-size: 10px; color: var(--muted); margin-top: 2px; }
  .divider { width: 1.5px; height: 66px; background: var(--teal-text); }
  .contact { list-style: none; font-size: 12px; color: var(--muted); }
  .contact li { display: flex; align-items: center; gap: 10px; line-height: 24px; }
  .contact svg { width: 13px; height: 13px; fill: var(--teal-text); }

  .card__stripe {
    position: absolute; left: 0; right: 0; bottom: 0; height: 22px;
    border-top: 4px solid var(--edge);
    background: linear-gradient(90deg, var(--sky), var(--lagoon));
  }
</style>
</head>
<body>
<main class="canvas">
  <section class="card card--front" aria-label="Card front">
    <div class="brand"><span class="brand__dot"></span>Tide Cove</div>
    <p class="website">www.tidecove.com</p>
  </section>

  <section class="card card--back" aria-label="Card back">
    <div class="brand"><span class="brand__dot"></span>Tide Cove</div>
    <div class="details">
      <div class="person">
        <p class="person__name">Mara Kessler</p>
        <p class="person__role">Law Attorney</p>
      </div>
      <span class="divider"></span>
      <ul class="contact">
        <li>
          <svg viewBox="0 0 16 16" aria-hidden="true"><path d="M1 6c2-4 12-4 14 0l-3 1-1-2H5L4 7z M4 8h8l2 6H2z"/></svg>
          (555) 014-2290
        </li>
        <li>
          <svg viewBox="0 0 16 16" aria-hidden="true"><path d="M1 3h14v10H1z M2 4l6 5 6-5" stroke="#fff" stroke-width="1.2"/></svg>
          mara@tidecove.com
        </li>
      </ul>
    </div>
    <div class="card__stripe"></div>
  </section>
</main>
</body>
</html>
```